Plan of Joint Exploration Venture

I need a multi page prospects design. A cover page, table of contents, and content pages. I'm looking for the basic design now for each page, with content to be filled in later. For now, you can use blank content or random content pulled from anywhere. The table of contents will include: Investment Overview, Details of the Offer, Details of the Strategy, and Management Team Bios. Please use the logo and pictures attached; also, I've attached a general example.

```html
<!DOCTYPE html>
<html lang="en">
<head>
<meta charset="utf-8">
<title>Investment Overview Spread</title>
<link rel="stylesheet" href="https://fonts.googleapis.com/css2?family=Arimo:wght@400;700&display=swap">
<style>
  :root {
    --backdrop: #e9e6e1;
    --paper: #f4f4f4;
    --brand-red: #b3121c;
    --brand-red-deep: #8f0d15;
    --ink-light: #ffffff;
    --photo-light: #f2f2f2;
    --photo-mid: #cfcfcf;
    --photo-dark: #8a8a8a;
  }
  * { box-sizing: border-box; margin: 0; padding: 0; }
  html, body {
    width: 1200px;
    height: 775px;
    overflow: hidden;
    background: var(--backdrop);
    font-family: "Arimo", Arial, sans-serif;
  }
  .spread {
    position: absolute;
    left: 140px;
    top: 72px;
    width: 920px;
    height: 630px;
    display: flex;
    box-shadow: 0 12px 30px rgba(0,0,0,0.18);
  }
  .page {
    position: relative;
    width: 460px;
    height: 630px;
    overflow: hidden;
  }
  .page--left {
    background: var(--paper);
  }
  .page--right {
    background: linear-gradient(90deg, var(--brand-red-deep) 0%, var(--brand-red) 6%, var(--brand-red) 100%);
  }
  .feature-photo {
    position: absolute;
    inset: 0;
    background: radial-gradient(ellipse at 55% 55%, var(--photo-light) 0%, var(--photo-mid) 55%, var(--photo-dark) 100%);
  }
  .section-tab {
    position: absolute;
    top: 22px;
    right: 0;
    width: 170px;
    height: 62px;
    background: var(--brand-red);
    border-radius: 31px 0 0 31px;
    color: var(--ink-light);
    font-weight: 700;
    font-size: 17px;
    line-height: 20px;
    letter-spacing: 0.5px;
    padding: 11px 0 0 24px;
    text-transform: uppercase;
  }
  .overview-text {
    position: absolute;
    top: 110px;
    left: 95px;
    width: 280px;
    color: var(--ink-light);
    font-size: 9px;
    line-height: 11.5px;
    text-align: justify;
  }
  .overview-text p { margin-bottom: 11px; }
</style>
</head>
<body>
  <main class="spread">
    <section class="page page--left">
      <div class="feature-photo" role="img" aria-label="Black and white photo of a hand dropping a coin into a glass light bulb filled with coins"></div>
      <h1 class="section-tab">Investment<br>Overview</h1>
    </section>
    <section class="page page--right">
      <div class="overview-text">
        <p>Northern Frontier is headquartered in Melbourne, Australia with a U.S. office in Denver, Colorado and as at the date of this Prospectus has acquired and entered into agreements to acquire leasehold interests across an aggregate of 56,550 Gross Acres, spanning 5 Projects. References in this Prospectus to acreage or land held or acquired or sold by Northern Frontier are references to leasehold interests. See Section 10 for a detailed explanation of land rights in the USA.</p>
        <p>Each of Northern Frontier's Projects are located within onshore USA. Northern Frontier is currently developing and exploring its leasehold interests, with a view to providing long-term growth in Shareholder value.</p>
        <p>Northern Frontier is an oil and natural gas exploration and development (E&amp;P) company geographically focused on oil and gas exploration and development opportunities in Rocky Mountain Basins which have become premier oil and gas productive regions in the USA.</p>
        <p>Northern Frontier has assembled a portfolio of prospective exploration assets. The portfolio contains a mix of exploration targets including:</p>
        <p>Northern Frontier has entered into an agreement to purchase a 90% Working Interest in the Ridgeback Project, at completion of which, Northern Frontier will hold mineral interests across an additional 6,633 Gross Acres (3,373 Net Acres). Northern Frontier is targeting short to medium term cashflow from its conventional oil prospects should its exploration program yield a commercial discovery. The Board considers that it has assembled a balanced portfolio of prospective exploration</p>
      </div>
    </section>
  </main>
</body>
</html>
```